flyer design for landscape group. i have enclosed my business card with logo

we are a local domestic and commercial landscaping group based in wokingham berkshire .we offer competitive landscaping solutions with a broad knowledge helping us solve problems in many fields such as new lawns, lawn care,tree care ,tree removal,hard and soft landscaping, decking, fencing ,garden or land clearance or just helping you with general maintanence. Being fully insured and certified for the job ,our excellent attention to detail has seen us recognised by local authorities and work for them on maintenance programmes performing in a safe and efficient manner

Target Market(s)

high end gardens commercial property

Industry/Entity Type

Landscaping

Requirements
Must have
• my logo . and some minimal sleek black and white design with small injections of colour
Should not have
• please do not include my full name or address only email and telephone

```html
<!DOCTYPE html>
<html lang="en">
<head>
<meta charset="utf-8">
<title>Fernwood Berkshire – Landscaping Flyer</title>
<link rel="stylesheet" href="https://fonts.googleapis.com/css2?family=Work+Sans:wght@300;400;700&family=Kaushan+Script&display=swap">
<style>
  :root {
    --page: #ffffff;
    --ivy-mono-dark: #262626;
    --ivy-mono-mid: #4a4a4a;
    --ivy-green-dark: #0f2a18;
    --ivy-green-mid: #2f5a35;
    --ivy-green-light: #4f7f4c;
    --ink-light: #ffffff;
    --ink-soft: rgba(255,255,255,0.92);
  }
  * { margin: 0; padding: 0; box-sizing: border-box; }
  html, body { width: 1200px; height: 872px; overflow: hidden; background: var(--page); }
  body { position: relative; font-family: "Work Sans", Arial, sans-serif; color: var(--ink-light); }

  .flyer { position: absolute; top: 63px; width: 527px; height: 746px; overflow: hidden; }
  .flyer--info { left: 50px; }
  .flyer--cover { left: 625px; }

  .flyer__photo { position: absolute; inset: 0; }
  .flyer--info .flyer__photo {
    background: radial-gradient(circle at 40% 35%, var(--ivy-mono-mid), var(--ivy-mono-dark) 75%);
  }
  .flyer--cover .flyer__photo {
    background: radial-gradient(circle at 45% 45%, var(--ivy-green-light), var(--ivy-green-mid) 45%, var(--ivy-green-dark) 100%);
  }

  .headline { position: absolute; left: 50px; top: 52px; line-height: 72px; font-size: 70px; letter-spacing: -1px; }
  .headline span { display: block; }
  .headline__light { font-weight: 300; }
  .headline__bold { font-weight: 700; }

  .rule { position: absolute; left: 0; top: 274px; width: 313px; height: 1px; background: var(--ink-light); }

  .location { position: absolute; left: 55px; top: 286px; font-size: 24px; font-weight: 300; }

  .about { position: absolute; left: 60px; top: 339px; width: 460px; font-size: 18px; font-weight: 300; line-height: 24px; color: var(--ink-soft); }
  .about p + p { margin-top: 24px; }

  .contact-title { position: absolute; left: 34px; top: 610px; font-family: "Kaushan Script", cursive; font-size: 36px; }

  .contact { position: absolute; font-size: 19px; font-weight: 300; line-height: 25px; }
  .flyer--info .contact { left: 69px; top: 665px; }
  .flyer--cover .contact { left: 0; right: 0; top: 665px; text-align: center; }

  .brand-small { position: absolute; left: 386px; top: 675px; width: 120px; text-align: center; font-size: 15px; font-weight: 400; letter-spacing: 1px; }
  .brand-small__dot { display: block; width: 28px; height: 28px; margin: 0 auto 8px; border: 1.5px solid var(--ink-light); border-radius: 50%; }

  .brand-large { position: absolute; left: 0; right: 0; top: 192px; text-align: center; font-weight: 300; }
  .brand-large__dot { display: block; width: 140px; height: 140px; margin: 0 auto 48px; border: 2px solid var(--ink-light); border-radius: 50%; }
  .brand-large__name { display: block; font-size: 54px; letter-spacing: 4px; line-height: 60px; }
  .brand-large__region { display: block; font-size: 23px; font-weight: 400; letter-spacing: 5px; margin-top: 12px; }

  .tagline { position: absolute; left: 0; right: 0; top: 582px; text-align: center; font-family: "Kaushan Script", cursive; font-size: 19px; line-height: 24px; }
</style>
</head>
<body>

  <section class="flyer flyer--info">
    <div class="flyer__photo" role="img" aria-label="Black and white photograph of dense ivy leaves"></div>

    <h1 class="headline">
      <span class="headline__light">Complete</span>
      <span class="headline__bold">Landscaping</span>
      <span class="headline__light">Solutions</span>
    </h1>
    <div class="rule"></div>
    <p class="location">Wokingham, Berkshire</p>

    <div class="about">
      <p>Whether it’s local domestic or commercial, we<br>offer competitive landscaping solutions with a<br>broad knowledge helping us solve problems in<br>many fields such as new lawn care, tree care &amp;<br>removal, hard &amp; soft landscaping, decking,<br>fencing, garden &amp; land clearance or just<br>helping you with general maintanence.</p>
      <p>You can be rest assured in the knowledge we<br>are fully insured and certified for the job.</p>
    </div>

    <h2 class="contact-title">Contact us</h2>
    <p class="contact">0700 900 4815<br>Sam@FernwoodBerkshire.co.uk</p>

    <div class="brand-small">
      <span class="brand-small__dot"></span>
      FERNWOOD
    </div>
  </section>

  <section class="flyer flyer--cover">
    <div class="flyer__photo" role="img" aria-label="Colour photograph of dense green ivy leaves"></div>

    <div class="brand-large">
      <span class="brand-large__dot"></span>
      <span class="brand-large__name">FERNWOOD</span>
      <span class="brand-large__region">BERKSHIRE</span>
    </div>

    <p class="tagline">Complete<br>Landscaping Solutions</p>
    <p class="contact">0700 900 4815<br>Sam@FernwoodBerkshire.co.uk</p>
  </section>

</body>
</html>
```